Corvane Holdings , new business card design

investment firm with corporate clients . need double sided business card , vertical and horizontal options ,logo must be clear. prefer pantone colors only and sharp design. website also www.corvane-demo.ae

Khalid Bin Rashed
Managing Director
Tel. +971 4 000 1234
Mobile +971 50 000 5678
khalid@corvane-demo.ae
Palmgate Tower, officw 18-B07, Noor Terraces, Dubai

Khalid Bin Rashed
Managing Director

Serif

Designer to choose colors to be used in the design.

```html
<!DOCTYPE html>
<html lang="en">
<head>
<meta charset="UTF-8">
<title>Corvane Holdings – Business Card</title>
<link rel="stylesheet" href="https://fonts.googleapis.com/css2?family=Poppins:ital,wght@0,400;0,600;1,400&display=swap">
<style>
  :root {
    --navy: #20225a;
    --navy-deep: #262968;
    --navy-mid: #353a7c;
    --ink: #2c2f55;
    --muted: #3d4063;
    --paper: #ffffff;
    --edge: #c9c9c9;
  }
  * { margin: 0; padding: 0; box-sizing: border-box; }
  html, body { width: 1200px; height: 1200px; overflow: hidden; background: var(--paper); }
  body { position: relative; font-family: "Poppins", sans-serif; }

  .card { position: absolute; left: 160px; width: 878px; height: 502px; overflow: hidden; }

  /* Front */
  .card--front { top: 81px; border: 1px solid var(--edge); background: var(--paper); }
  .brand-mark {
    position: absolute; left: 46px; top: 50px;
    font-weight: 400; font-size: 30px; letter-spacing: 9px;
    color: var(--navy); text-transform: uppercase; white-space: nowrap;
  }
  .contact-list {
    position: absolute; left: 557px; top: 44px; list-style: none;
    font-style: italic; font-size: 23px; line-height: 30px; color: var(--muted);
  }
  .contact-list li { display: flex; align-items: center; gap: 10px; }
  .contact-list svg { width: 16px; height: 18px; flex: none; }
  .contact-list .email { padding-left: 0; }
  .holder { position: absolute; left: 0; right: 0; top: 212px; text-align: center; }
  .holder__name {
    display: inline-block; font-weight: 600; font-size: 36px; color: var(--ink);
    padding: 0 8px 2px; border-bottom: 2px solid var(--navy-mid); line-height: 48px;
  }
  .holder__role { font-size: 27px; color: var(--muted); margin-top: 2px; }
  .front-rules { position: absolute; left: 0; right: 0; top: 440px; height: 10px; }
  .address-band {
    position: absolute; left: 0; right: 0; bottom: 0; height: 53px; background: var(--navy);
    display: flex; align-items: center; justify-content: center; gap: 8px;
    color: #fff; font-style: italic; font-size: 19px; letter-spacing: 0.3px;
  }
  .address-band svg { width: 16px; height: 20px; }

  /* Back */
  .card--back { top: 637px; background: var(--navy-deep); }
  .skyline {
    position: absolute; inset: 0;
    background: linear-gradient(180deg, #272a69 0%, #2f3478 45%, #323a80 65%, #23265f 100%);
  }
  .back-brand {
    position: absolute; left: 0; right: 0; top: 220px; text-align: center;
    font-weight: 400; font-size: 46px; letter-spacing: 12px; color: #fff;
    text-transform: uppercase; white-space: nowrap;
  }
  .back-site {
    position: absolute; left: 0; right: 0; bottom: 20px; text-align: center;
    font-style: italic; font-size: 31px; letter-spacing: 1px; color: #fff;
  }
</style>
</head>
<body>
  <section class="card card--front">
    <div class="brand-mark">Corvane Holdings</div>

    <ul class="contact-list">
      <li>
        <svg viewBox="0 0 16 18"><path d="M4 2l3 4-2 2c1 2 3 4 5 5l2-2 4 3-2 3C7 17 1 10 1 4z" fill="#3d4063"/></svg>
        +971-4-000-1234
      </li>
      <li>
        <svg viewBox="0 0 16 18"><rect x="3" y="1" width="10" height="16" rx="1.5" fill="none" stroke="#3d4063" stroke-width="1.5"/></svg>
        +971-50-000-5678
      </li>
      <li class="email">khalid@corvane-demo.ae</li>
    </ul>

    <div class="holder">
      <div class="holder__name">Khalid Bin Rashed</div>
      <div class="holder__role">Managing Director</div>
    </div>

    <svg class="front-rules" viewBox="0 0 878 10" preserveAspectRatio="none">
      <line x1="0" y1="1" x2="878" y2="1" stroke="#20225a" stroke-width="1.5"/>
      <line x1="0" y1="5" x2="878" y2="5" stroke="#20225a" stroke-width="1"/>
      <line x1="0" y1="9" x2="878" y2="9" stroke="#20225a" stroke-width="1"/>
    </svg>

    <div class="address-band">
      <svg viewBox="0 0 16 20"><path d="M8 0a7 7 0 0 0-7 7c0 5 7 13 7 13s7-8 7-13a7 7 0 0 0-7-7zm0 10a3 3 0 1 1 0-6 3 3 0 0 1 0 6z" fill="#fff"/></svg>
      Palmgate Tower, officw 18-B07, Noor Terraces, Dubai
    </div>
  </section>

  <section class="card card--back">
    <div class="skyline" role="img" aria-label="Monochrome navy illustration of a city skyline with towers and a curving road"></div>
    <div class="back-brand">Corvane Holdings</div>
    <div class="back-site">www.corvane-demo.ae</div>
  </section>
</body>
</html>
```